Southport Billboard for Hiring more CDL drivers

I need a catch design for a bill board (size 10ft by 36 ft) to catch the attention for semi truck drivers.
In the design I want it to include:
-My company logo along with my website(brisklanefreighters.com) and my number(503-217-6095) for contact info.
-I also need it to say earn up to $90,000 a year
-I will send a few photos to choose from
-I need the logo to look clean and simple! I don't want it to be cluttered just clean, simple and catchy.!

Target Market(s)

CDL Class A holders
Semi Truck Drivers

Industry/Entity Type

Trucking Company

Font styles to use
Other font styles liked:
• a font to match my logo

Requirements
Must have
• "Make up to $90,000"
"brisklanefreighters.com"
"503-217-6095"

```html
<!DOCTYPE html>
<html lang="en">
<head>
<meta charset="UTF-8">
<title>Brisklane Freighters – Driver Hiring Billboard</title>
<link rel="stylesheet" href="https://fonts.googleapis.com/css2?family=Anton&family=Montserrat:wght@500;700&display=swap">
<style>
  :root {
    --stage: #2b3550;
    --ink: #161616;
    --white: #ffffff;
    --amber: #f9ab22;
    --sky-top: #6f9cc9;
    --sky-mid: #b9c9d6;
    --haze: #8e9aa5;
    --skyline: #9aa6b0;
    --road: #34383d;
    --road-dark: #1c1e21;
    --truck-teal: #3b9fbf;
    --truck-chrome: #c9ced2;
    --truck-red: #9c2f3a;
  }
  * { margin: 0; padding: 0; box-sizing: border-box; }
  html, body {
    width: 1200px;
    height: 709px;
    overflow: hidden;
    background: var(--stage);
  }
  .billboard {
    position: absolute;
    left: 0;
    top: 188px;
    width: 1200px;
    height: 333px;
    overflow: hidden;
  }
  .billboard-photo {
    position: absolute;
    inset: 0;
    background: linear-gradient(to bottom,
      var(--sky-top) 0%,
      var(--sky-mid) 45%,
      var(--haze) 66%,
      var(--road) 74%,
      var(--road-dark) 100%);
  }
  .skyline {
    position: absolute;
    left: 0;
    right: 0;
    top: 150px;
    height: 85px;
    background: linear-gradient(to bottom, rgba(154,166,176,0) 0%, var(--skyline) 55%, rgba(120,130,140,0.9) 100%);
  }
  .trucks {
    position: absolute;
    left: 423px;
    top: 114px;
    width: 352px;
    height: 163px;
    border-radius: 6px 6px 14px 14px;
    background: linear-gradient(to right,
      var(--truck-teal) 0%,
      var(--truck-chrome) 30%,
      var(--truck-teal) 48%,
      var(--truck-red) 52%,
      var(--truck-chrome) 72%,
      var(--truck-red) 100%);
  }
  .brand-panel {
    position: absolute;
    left: 124px;
    top: 17px;
    width: 303px;
    height: 97px;
    background: var(--white);
    display: flex;
    flex-direction: column;
    align-items: center;
    justify-content: center;
    font-family: "Anton", sans-serif;
    color: var(--ink);
    line-height: 1;
  }
  .brand-name { font-size: 40px; letter-spacing: 1px; }
  .brand-sub { font-size: 15px; letter-spacing: 5px; margin-top: 4px; }
  .headline-panel {
    position: absolute;
    left: 427px;
    top: 17px;
    width: 649px;
    height: 97px;
    background: var(--amber);
    display: flex;
    align-items: center;
    justify-content: center;
  }
  .headline {
    font-family: "Anton", sans-serif;
    font-size: 64px;
    font-weight: 400;
    color: var(--ink);
    letter-spacing: 4px;
    line-height: 1;
  }
  .contact-row {
    position: absolute;
    left: 0;
    right: 0;
    top: 276px;
    height: 46px;
    display: flex;
    align-items: center;
    justify-content: center;
    gap: 18px;
    color: var(--white);
    font-family: "Montserrat", sans-serif;
  }
  .rule { width: 110px; height: 3px; background: var(--white); }
  .phone { font-size: 40px; font-weight: 700; letter-spacing: 0.5px; }
  .divider { width: 2px; height: 38px; background: var(--white); }
  .website { font-size: 33px; font-weight: 500; }
</style>
</head>
<body>
  <section class="billboard">
    <div class="billboard-photo" role="img" aria-label="Open highway under a pale blue sky"></div>
    <div class="skyline" role="img" aria-label="Hazy city skyline along both sides of the highway"></div>
    <div class="trucks" role="img" aria-label="Two semi trucks side by side facing forward, one teal and one red, with chrome grilles"></div>
    <div class="brand-panel">
      <span class="brand-name">BRISKLANE</span>
      <span class="brand-sub">FREIGHTERS</span>
    </div>
    <div class="headline-panel">
      <h1 class="headline">MAKE UP TO $90,000</h1>
    </div>
    <div class="contact-row">
      <span class="rule"></span>
      <span class="phone">503-217-6095</span>
      <span class="divider"></span>
      <span class="website">brisklanefreighters.com</span>
      <span class="rule"></span>
    </div>
  </section>
</body>
</html>
```